Swimming Pool Service business card needed!!!! Please

Hi Everyone! Thanks for looking at my contest. I PROMISE to provide excellent feedback during this process.

I am starting a new swimming pool cleaning business in San Diego, California and would like your help in making a business card for me.

I like easy to read, classy and sophisticated.

I am having a website designed and I'm looking for it to have pictures of really clean & clear pools.

I really like the blue on white color format, but open to other colors.

I do not have a logo, but the name of my company is GLIMMERTIDE POOL SERVICE.

My tag line is: Pools so clean, you can see yourself "in" them. (does not need to have the quotes around "in"...maybe just italics for this word IN?) You decide for me.

I would like to have a logo designed that incorporates some sort of easy to read letters. I do not want cursive (handwriting) letters. I thought about having a "reflection" of letters (mirror image), but think that this will be hard to read from far away. Maybe you can surprise me and come up with an idea that works using the a mirror image....but I'm not sure. I was leaning toward plain old BLOCK letters as I think it would be easy to read on my truck.

I would like to have the NAQTR and WBK logos on the back of the card. I have attached those two as files. You can put other things on the back as well, but I need these two logos on there. Or maybe put them on the front of the card if you have a better idea for the back of the card! :-)

Maybe blue on the back of the card and white on the front of the card? I don't know, I'm just thinking out loud.

I had another card done awhile ago called HARBORLINE TEES. I have uploaded a copy of that card for your reference. I don't want this card to be the same as my new company is a swimming pool cleaning company, but I wanted you to see what I liked in the past.

THANK YOU!!!!
Updates

Reason: Partner out of town and want their feedback....so need more time to decide and designs still coming in.

Industry/Entity Type

Business

Contact Information for Business Card

GLIMMERTIDE POOL SERVICE
Dale Wexby
Owner
4817 Quarry Bend Ave. #512
San Diego, CA 92417
858-291-6083
www.glimmertidepoolservice.example

Font styles to use
Sans Serif

Colors
0255a3
3176b5
ffffff

Requirements
Nice to have
• Some things to (possibly) add to back of card (in no particular order)
• WBK logo
• NAQTR logo
• Free Estimates
• Residential and Commercial Services
• Equipment Repairs
• Saltwater Systems
• Licensed, Bonded, Insured
• Family Owned and Operated
• No Contracts
• =======================
• Check out the FolioMint business card that i attached.
• i think they did this using a chrome overlay.
• Can any of you guys design that? or is that done at my printer?
• ==================
Should not have
• Hi Designers-
• The first round of cards came back and let's stay away from the light blue (powder blue) color. I don't like the look of it on the business cards.
• Also, the pool company JPG's that I attached are other logos of pool companies that I liked. I don't want them to be on my card. The only logos that should be on my card are the one you are going to come up with for my company, the WBK logo and the NAQTR logo.
• Lastly, no vertical cards and no split cards (logo on left, contact info on right side).
• Thanks much!

```html
<!DOCTYPE html>
<html lang="en">
<head>
<meta charset="utf-8">
<title>Glimmertide Pool Service – Business Card</title>
<link rel="stylesheet" href="https://fonts.googleapis.com/css2?family=Questrial&family=Open+Sans:wght@400&display=swap">
<style>
  :root {
    --brand-blue: #0255a3;
    --mid-blue: #3176b5;
    --soft-blue: #8fb7dd;
    --pale-blue: #dbe7f0;
    --list-blue: #a9c8e8;
    --white: #ffffff;
    --page: #ffffff;
  }
  html, body {
    margin: 0;
    width: 1200px;
    height: 1200px;
    overflow: hidden;
    background: var(--page);
  }
  .sheet {
    position: relative;
    width: 1200px;
    height: 1200px;
  }
  .card {
    position: absolute;
    left: 322px;
    width: 551px;
    height: 310px;
    overflow: hidden;
    box-shadow: 8px 9px 10px rgba(0,0,0,0.22);
    font-family: "Questrial", sans-serif;
  }
  .card--front {
    top: 201px;
    background: var(--white);
    border: 1px solid #8a8a8a;
    box-sizing: border-box;
  }
  .card--back {
    top: 582px;
    background: var(--brand-blue);
  }

  /* brand lockup */
  .brand {
    position: absolute;
    text-align: center;
    color: var(--brand-blue);
    font-family: "Questrial", sans-serif;
    font-weight: 400;
    line-height: 1;
  }
  .brand__dot {
    display: block;
    margin: 0 auto 12px;
    width: 48px;
    height: 48px;
    border-radius: 50%;
    background: currentColor;
  }
  .brand__name {
    display: block;
    font-size: 25px;
    letter-spacing: 2px;
  }
  .brand__sub {
    display: block;
    margin-top: 6px;
    font-size: 15px;
    letter-spacing: 2.5px;
  }
  .card--front .brand { left: 36px; top: 30px; width: 218px; }
  .card--back .brand { left: 0; right: 0; top: 28px; color: var(--white); }

  /* front */
  .front__arc {
    position: absolute;
    left: 0; top: 0;
  }
  .person {
    position: absolute;
    right: 42px;
    top: 124px;
    text-align: right;
  }
  .person__name {
    font-family: "Open Sans", sans-serif;
    font-size: 28px;
    color: var(--brand-blue);
    line-height: 1;
  }
  .person__title {
    margin-top: 10px;
    margin-right: 12px;
    font-size: 13px;
    letter-spacing: 3px;
    color: var(--mid-blue);
  }
  .contact {
    position: absolute;
    right: 40px;
    top: 208px;
    text-align: right;
    font-size: 14px;
    letter-spacing: 1.2px;
    color: var(--mid-blue);
    line-height: 21px;
  }
  .web-band {
    position: absolute;
    left: 0; right: 0;
    top: 264px;
    height: 20px;
    background: var(--brand-blue);
    color: var(--white);
    text-align: center;
    font-size: 14px;
    letter-spacing: 1.8px;
    line-height: 20px;
  }

  /* back */
  .services {
    position: absolute;
    left: 32px;
    top: 170px;
    margin: 0;
    padding: 0;
    list-style: none;
    font-size: 14px;
    letter-spacing: 1.6px;
    line-height: 16.5px;
    color: var(--list-blue);
  }
  .services li::before { content: "- "; }
  .badge {
    position: absolute;
    width: 56px;
    height: 56px;
    border-radius: 50%;
    background: var(--white);
    border: 3px solid var(--pale-blue);
    box-sizing: border-box;
  }
  .badge--first { left: 387px; top: 223px; }
  .badge--second { left: 457px; top: 223px; }
</style>
</head>
<body>
<main class="sheet">

  <section class="card card--front" aria-label="Business card front">
    <svg class="front__arc" width="551" height="310" viewBox="0 0 551 310" aria-hidden="true">
      <ellipse cx="548" cy="141" rx="228" ry="46" fill="none" stroke="var(--pale-blue)" stroke-width="14"/>
    </svg>

    <div class="brand">
      <span class="brand__dot"></span>
      <span class="brand__name">GLIMMERTIDE</span>
      <span class="brand__sub">POOL SERVICE</span>
    </div>

    <div class="person">
      <div class="person__name">Dale Wexby</div>
      <div class="person__title">Owner</div>
    </div>

    <address class="contact" style="font-style:normal">
      4817 Quarry Bend Ave. #512 San Diego, CA<br>
      (858)-291-6083
    </address>

    <div class="web-band">www.glimmertidepoolservice.example</div>
  </section>

  <section class="card card--back" aria-label="Business card back">
    <div class="brand">
      <span class="brand__dot"></span>
      <span class="brand__name">GLIMMERTIDE</span>
      <span class="brand__sub">POOL SERVICE</span>
    </div>

    <ul class="services">
      <li>Free Estimates</li>
      <li>Residential and Commercial Services</li>
      <li>Equipment Repairs</li>
      <li>Saltwater Systems</li>
      <li>Licensed, Bonded, Insured</li>
      <li>Family Owned and Operated</li>
      <li>No Contracts</li>
    </ul>

    <span class="badge badge--first" role="img" aria-label="WBK certification badge"></span>
    <span class="badge badge--second" role="img" aria-label="NAQTR membership badge"></span>
  </section>

</main>
</body>
</html>
```